Webdesign project for healthcare IT company

Home, About, Solution, Contact, and Employment pages.

Please match the designs uploaded for colors and effect.

Please choose appropriate healthcare IT related photos to the content. Be sure to include the content that i've attached in the word document.

Please use the following URLs as reference:

www.morvilcare.example
www.tovrix.example
www.pelmaragree.example

Target Market(s)

healthcare providers, doctors, nurses, c-level executives

Industry/Entity Type

Healthcare

Coding

Coded - Design and coding required

Number of Pages Required

5+ page

Font styles to use
Serif
Sans Serif

Colors
6b449b
0455a3
ffffff
333333
959595

Requirements
Must have
• B2B feel, matches the colors in the uploaded design files, images that can be purchased later that meet the content that I've uploaded

```html
<!DOCTYPE html>
<html lang="en">
<head>
<meta charset="utf-8">
<title>Vigil Technologies</title>
<link href="https://fonts.googleapis.com/css2?family=Poppins:wght@400;500;600&display=swap" rel="stylesheet">
<style>
  :root {
    --purple: #6b449b;
    --blue: #0455a3;
    --title-blue: #2747a0;
    --ink: #333333;
    --grey: #959595;
    --text: #555555;
    --white: #ffffff;
    --band: #f4f4f4;
    --footer: #3c3535;
  }
  * { margin: 0; padding: 0; box-sizing: border-box; }
  html, body { width: 827px; height: 1200px; overflow: hidden; }
  body { font-family: "Poppins", sans-serif; background: var(--white); color: var(--ink); position: relative; }

  .site-header { position: absolute; top: 0; left: 0; width: 827px; height: 58px; background: var(--white); }
  .brand { position: absolute; left: 60px; top: 19px; display: flex; align-items: center; gap: 7px; }
  .brand-mark { width: 14px; height: 14px; background: var(--purple); }
  .brand-name { font-size: 15px; font-weight: 600; color: var(--purple); letter-spacing: 0.3px; }
  .main-nav { position: absolute; top: 22px; left: 440px; display: flex; gap: 27px; font-size: 11px; color: var(--ink); }
  .main-nav a { color: inherit; text-decoration: none; position: relative; }
  .main-nav a.active::after { content: ""; position: absolute; left: 1px; right: 1px; top: 34px; height: 2px; background: var(--purple); }

  .hero { position: absolute; top: 58px; left: 0; width: 827px; height: 374px; }
  .hero-photo { position: absolute; inset: 0; background: radial-gradient(ellipse at 40% 60%, #5f86ad 0%, #3d6a99 45%, #2d5288 100%); }
  .hero-content { position: absolute; top: 114px; left: 0; width: 827px; text-align: center; color: var(--white); }
  .hero-kicker { font-size: 17px; font-weight: 400; }
  .hero-title { font-size: 34px; font-weight: 600; line-height: 1.2; margin-top: 0; }
  .hero-lead { width: 620px; margin: 15px auto 0; font-size: 9.5px; line-height: 15px; }

  .what-we-do { position: absolute; top: 432px; left: 0; width: 827px; height: 312px; background: var(--band); }
  .section-heading { font-size: 18px; font-weight: 500; color: var(--ink); }
  .what-we-do .section-heading { position: absolute; left: 59px; top: 36px; }
  .what-we-do .rule { position: absolute; left: 59px; top: 63px; width: 20px; height: 1px; background: var(--purple); }
  .what-copy { position: absolute; left: 59px; top: 78px; width: 460px; font-size: 9.5px; line-height: 15.2px; color: var(--text); }
  .what-copy p + p { margin-top: 15px; }
  .what-photo { position: absolute; left: 546px; top: 34px; width: 221px; height: 242px; background: linear-gradient(135deg, #1a5fe0, #0b3fb8 60%, #1c58d0); }

  .services { position: absolute; top: 744px; left: 0; width: 827px; }
  .services .section-heading { position: absolute; top: 32px; width: 827px; text-align: center; font-size: 21px; }
  .services .rule { position: absolute; top: 63px; left: 397px; width: 32px; height: 1px; background: var(--purple); }
  .service { position: absolute; top: 86px; width: 214px; text-align: center; }
  .service-photo { width: 214px; height: 185px; }
  .service-title { margin-top: 20px; font-size: 15px; font-weight: 500; color: var(--title-blue); }
  .service-text { margin: 12px auto 0; width: 200px; font-size: 9.5px; line-height: 15.2px; color: var(--text); }
  .svc-1 { left: 59px; } .svc-1 .service-photo { background: linear-gradient(160deg, #6fb3a5, #d8d2c0 55%, #7a5038); }
  .svc-2 { left: 306px; } .svc-2 .service-photo { background: linear-gradient(150deg, #f1f1f1, #cfcfcf 50%, #ececec); }
  .svc-3 { left: 553px; } .svc-3 .service-photo { background: linear-gradient(180deg, #6d4e3a, #e2562c 50%, #4d8fd0); }

  .site-footer { position: absolute; top: 1162px; left: 0; width: 827px; height: 38px; background: var(--footer); color: var(--white); }
  .copyright { position: absolute; left: 59px; top: 13px; font-size: 9px; }
  .social { position: absolute; right: 60px; top: 14px; display: flex; gap: 10px; }
  .social span { width: 9px; height: 9px; border-radius: 50%; background: var(--white); }
</style>
</head>
<body>
  <header class="site-header">
    <div class="brand"><span class="brand-mark"></span><span class="brand-name">Vigil Technologies</span></div>
    <nav class="main-nav">
      <a class="active" href="#">Home</a>
      <a href="#">About</a>
      <a href="#">Solution</a>
      <a href="#">Contact</a>
      <a href="#">Employment</a>
    </nav>
  </header>

  <section class="hero">
    <div class="hero-photo" role="img" aria-label="Blurred 3D printed lattice objects on a table under a blue tint"></div>
    <div class="hero-content">
      <p class="hero-kicker">It’s time to wake up with</p>
      <h1 class="hero-title">Vigil Technologies</h1>
      <p class="hero-lead">Disruption isn’t just coming – it’s already here and it’s time to wake up to the new world we live in. Here at Vigil Technologies, we embrace the future that disruption brings and make it our aim to assist the world in embracing this bright future with us. We help bring businesses and people adapt to new approaches to old problems.</p>
    </div>
  </section>

  <section class="what-we-do">
    <h2 class="section-heading">What We Do</h2>
    <div class="rule"></div>
    <div class="what-copy">
      <p>We are engineers, problem-solvers, people persons, and a friendly face. We want to solve your problem in a way that won’t break the bank, give headaches, leave you with a smile on your face, and keep you smiling throughout our relationship.</p>
      <p>We predominantly work in the healthcare IT industry assisting hospitals and clinics with their IT infrastructure and information workflows. We provide software solutions and interoperability services to connect platforms and give care givers a simple view of patient records.</p>
      <p>Vigil Technologies is also exploring the world of 3D printing and how it can fully affect the healthcare industry and small businesses with Vigil3D. 3D printing is a great solution to what used to be a very niche industry.</p>
    </div>
    <div class="what-photo" role="img" aria-label="Blue 3D printer illustration with large 3D lettering"></div>
  </section>

  <section class="services">
    <h2 class="section-heading">Our Services</h2>
    <div class="rule"></div>
    <article class="service svc-1">
      <div class="service-photo" role="img" aria-label="Vintage beige computer terminal on a wooden desk"></div>
      <h3 class="service-title">Computer Archeology</h3>
      <p class="service-text">Need data off a legacy system that you would like to sunset? We can help you with that.</p>
    </article>
    <article class="service svc-2">
      <div class="service-photo" role="img" aria-label="Tablet on a white desk beside a keyboard and pens"></div>
      <h3 class="service-title">Digital Check In</h3>
      <p class="service-text">Still using clipboards to check people into your facility? Struggling to get that paper-based information into your system? We can help you with that.</p>
    </article>
    <article class="service svc-3">
      <div class="service-photo" role="img" aria-label="3D printer printing a red and orange vase"></div>
      <h3 class="service-title">Vigil3D</h3>
      <p class="service-text">Have something in mind that you need printed, but don’t have a 3D printer? We can help you design it, and print it for you.</p>
    </article>
  </section>

  <footer class="site-footer">
    <p class="copyright">© 2018 &nbsp;| ALL RIGHTS RESERVED.</p>
    <div class="social">
      <span role="img" aria-label="Social link"></span>
      <span role="img" aria-label="Social link"></span>
      <span role="img" aria-label="Social link"></span>
    </div>
  </footer>
</body>
</html>
```